Business Card

I need a business card that really pops for a potential customer or person who refers a personal injury lead. I want to highlight our office locations, but only address that needs to be on the card is my office's main address. I want a sleek, modern and minimalist design.

```html
<!DOCTYPE html>
<html lang="en">
<head>
<meta charset="UTF-8">
<title>Northfield Injury Lawyers – Business Card</title>
<link rel="stylesheet" href="https://fonts.googleapis.com/css2?family=Open+Sans:wght@300;400;700&display=swap">
<style>
  :root {
    --page-bg: #dcdddf;
    --card-light: #ffffff;
    --card-dark: #3b3b3b;
    --ink: #2e2e2e;
    --ink-soft: #3c3c3c;
    --rule: #4a4a4a;
    --logo-ink: #f4f4f4;
  }
  * { box-sizing: border-box; margin: 0; padding: 0; }
  html, body {
    width: 1200px;
    height: 780px;
    overflow: hidden;
    background: var(--page-bg);
    font-family: "Open Sans", Arial, sans-serif;
    color: var(--ink);
  }
  .canvas {
    width: 1200px;
    height: 780px;
    display: flex;
    align-items: center;
    justify-content: center;
    gap: 60px;
  }
  .card {
    width: 525px;
    height: 300px;
    position: relative;
    box-shadow: 0 8px 24px rgba(0,0,0,0.18);
  }

  /* Front face */
  .card-front { background: var(--card-light); }
  .identity {
    position: absolute;
    left: 44px;
    top: 98px;
    text-align: right;
  }
  .identity-name {
    font-weight: 700;
    font-size: 33px;
    letter-spacing: 0.2px;
    line-height: 1;
    color: var(--ink);
  }
  .identity-role {
    font-size: 12px;
    font-weight: 400;
    color: var(--ink-soft);
    margin-top: 3px;
  }
  .divider {
    position: absolute;
    left: 300px;
    top: 62px;
    width: 1px;
    height: 98px;
    background: linear-gradient(to bottom, transparent, var(--rule) 20%, var(--rule) 80%, transparent);
  }
  .contact-list {
    position: absolute;
    left: 326px;
    top: 74px;
    list-style: none;
  }
  .contact-item {
    display: flex;
    align-items: center;
    gap: 8px;
    font-size: 11.5px;
    line-height: 1;
    height: 23px;
    color: var(--ink);
  }
  .contact-item svg { width: 11px; height: 11px; flex: none; }
  .address {
    position: absolute;
    left: 0;
    right: 0;
    bottom: 50px;
    text-align: center;
    font-size: 13px;
    color: var(--ink);
  }

  /* Back face */
  .card-back {
    background: var(--card-dark);
    display: flex;
    align-items: center;
    justify-content: center;
  }
  .brand-name {
    color: var(--logo-ink);
    font-weight: 300;
    font-size: 22px;
    letter-spacing: 5px;
    text-transform: uppercase;
    white-space: nowrap;
  }
</style>
</head>
<body>
<main class="canvas">
  <section class="card card-front" aria-label="Business card front">
    <div class="identity">
      <div class="identity-name">Carver Ellison</div>
      <div class="identity-role">Lawyers</div>
    </div>
    <div class="divider"></div>
    <ul class="contact-list">
      <li class="contact-item">
        <svg viewBox="0 0 24 24" aria-hidden="true"><path fill="#333" d="M6.6 10.8a15.1 15.1 0 0 0 6.6 6.6l2.2-2.2c.3-.3.7-.4 1-.2 1.1.4 2.3.6 3.6.6.6 0 1 .4 1 1V20c0 .6-.4 1-1 1A17 17 0 0 1 3 4c0-.6.4-1 1-1h3.5c.6 0 1 .4 1 1 0 1.3.2 2.5.6 3.6.1.3 0 .7-.2 1z"/></svg>
        +1 312-555-0148
      </li>
      <li class="contact-item">
        <svg viewBox="0 0 24 24" aria-hidden="true"><rect x="2" y="5" width="20" height="14" rx="2" fill="#333"/><path d="M3 6l9 7 9-7" stroke="#fff" stroke-width="1.8" fill="none"/></svg>
        info@northfieldinjurylaw.com
      </li>
      <li class="contact-item">
        <svg viewBox="0 0 24 24" aria-hidden="true"><circle cx="12" cy="12" r="10" fill="#333"/><path d="M2 12h20M12 2c3 3 3 17 0 20M12 2c-3 3-3 17 0 20" stroke="#fff" stroke-width="1.3" fill="none"/></svg>
        www.northfieldinjurylaw.com
      </li>
    </ul>
    <p class="address">210 W. Harbor Drive, Suite 1800, Chicago, IL, United States, Illinois</p>
  </section>

  <section class="card card-back" aria-label="Business card back">
    <div class="brand-name">Northfield Injury Lawyers</div>
  </section>
</main>
</body>
</html>
```